Organic rose water based skincare line in need of product label and packaging design

We are looking for a simple, clean, modern labeling and packaging design for 2 of our products. Our brand's demographic is upscale females ages 20-40. We want our packaging to be very minimalistic, and instagramable.

Product #1: Rose water facial spray "Lumi Mist"
Product #2: Rose water facial toner "Velvet Hush Hour"

Please see attached images for our current logo and label design. We have also added some images that inspire our branding.

Target Market(s)

trendy woman ages 20-40

Industry/Entity Type

Skin Care Product

Font styles to use
Serif
Sans Serif

Colors

Designer to choose only greyscale colors for use in the design.

Requirements
Must have
• Must have our logo, bottle size, product name on front and how to use and ingredient on the back. Please see project description and attached images for more information.
Should not have
• Too much going on or too many colors.

```html
<!DOCTYPE html>
<html lang="en">
<head>
<meta charset="utf-8">
<title>Lumi Mist – Label Front and Back</title>
<link href="https://fonts.googleapis.com/css2?family=Questrial&display=swap" rel="stylesheet">
<style>
  :root {
    --stage: #000000;
    --label: #ffffff;
    --ink: #5a5a5c;
    --ink-soft: #6b6b6d;
    --band: #58585a;
    --band-text: #ffffff;
    --photo-light: #f2f2f2;
    --photo-mid: #bdbdbd;
    --photo-dark: #3a3a3a;
  }
  * { box-sizing: border-box; margin: 0; padding: 0; }
  html, body {
    width: 1200px; height: 1200px; overflow: hidden;
    background: var(--stage);
  }
  .canvas {
    position: relative; width: 1200px; height: 1200px;
    font-family: "Questrial", "Helvetica Neue", Arial, sans-serif;
    color: var(--ink);
  }
  .label {
    position: absolute; top: 135px; width: 469px; height: 933px;
    background: var(--label); border-radius: 30px; overflow: hidden;
    text-align: center;
  }
  .label--front { left: 107px; }
  .label--back { left: 623px; }

  /* front */
  .brand-mark {
    position: absolute; top: 250px; left: 0; right: 0;
    display: flex; flex-direction: column; align-items: center; gap: 14px;
  }
  .brand-mark__dot {
    width: 44px; height: 44px; border-radius: 50%;
    border: 2px solid var(--ink);
  }
  .brand-mark__name {
    font-size: 30px; line-height: 1.05; color: var(--ink);
  }
  .product-name {
    position: absolute; top: 352px; left: 0; right: 0;
    font-size: 82px; line-height: 1.02; letter-spacing: 2px;
    color: var(--ink); font-weight: 400;
  }
  .product-details {
    position: absolute; top: 546px; left: 0; right: 0;
    font-size: 24px; line-height: 1.12; color: var(--ink-soft);
  }
  .photo {
    position: absolute; left: 0; right: 0;
  }
  .photo--front-bottom {
    top: 640px; bottom: 0;
    background: linear-gradient(to bottom, var(--label) 0%, var(--photo-light) 15%, var(--photo-mid) 55%, var(--photo-dark) 100%);
  }
  .photo--back-top {
    top: 0; height: 350px;
    background: linear-gradient(to bottom, var(--photo-dark) 0%, var(--photo-mid) 45%, var(--photo-light) 80%, var(--label) 100%);
  }

  /* back */
  .directions {
    position: absolute; top: 368px; left: 0; right: 0;
    font-size: 25px; line-height: 1.16; color: var(--ink);
  }
  .ingredient-band {
    position: absolute; top: 491px; left: 0; right: 0; height: 69px;
    background: var(--band); color: var(--band-text);
    font-size: 35px; line-height: 69px;
  }
  .benefits {
    position: absolute; top: 573px; left: 0; right: 0;
    list-style: none; font-size: 26px; line-height: 41px; color: var(--ink);
  }
  .brand-mark--small {
    top: 838px; gap: 6px;
  }
  .brand-mark--small .brand-mark__dot { width: 22px; height: 22px; border-width: 1.5px; }
  .brand-mark--small .brand-mark__name { font-size: 14px; }
</style>
</head>
<body>
<main class="canvas">
  <section class="label label--front" aria-label="Front label">
    <div class="brand-mark brand-mark--large" style="top:190px">
      <span class="brand-mark__dot"></span>
      <span class="brand-mark__name">the petal studio</span>
    </div>
    <h1 class="product-name">LUMI<br>MIST</h1>
    <p class="product-details">Organic rosewater<br>hydrating mist<br>2 oz / 60 mL</p>
    <div class="photo photo--front-bottom" role="img" aria-label="Black and white photograph of garden roses and leaves on white wooden boards"></div>
  </section>

  <section class="label label--back" aria-label="Back label">
    <div class="photo photo--back-top" role="img" aria-label="Black and white photograph of garden roses and leaves on white wooden boards"></div>
    <p class="directions">mist over<br>face + body + hair<br>as desired for hydration</p>
    <div class="ingredient-band">organic / rose / water</div>
    <ul class="benefits">
      <li>+ hydrates</li>
      <li>+ fights acne</li>
      <li>+ maintains skin’s pH</li>
      <li>+ strengthens skin cells</li>
      <li>+ prevents fine lines &amp;<br>wrinkles</li>
    </ul>
    <div class="brand-mark brand-mark--small">
      <span class="brand-mark__dot"></span>
      <span class="brand-mark__name">the petal studio</span>
    </div>
  </section>
</main>
</body>
</html>
```